Business Card Design Project

Hello Designers, hope you are all aiming enjoy the weekend
I have the Business Logo (uploaded), you can alter the color which ever way you think would work,
Im looking for a simple yet striking feel, something which will stay memorable (I have uploaded 3 examples for you to flick through)
Information on the card, will just be the bare minimum,
Double Sided
Info being
i.e.
Name
Number
Website
ABN
Teo Marlowick
+482710365 (singapore)
+615093284 (Australia)
+790428153 (America)
www.lumoren-match.example
ABN 90817263
Enjoy,
Teo

```html
<!DOCTYPE html>
<html lang="en">
<head>
<meta charset="utf-8">
<title>Lumoren Match – Business Card</title>
<link rel="stylesheet" href="https://fonts.googleapis.com/css2?family=Quicksand:wght@500&family=PT+Sans:wght@400&display=swap">
<style>
  :root {
    --backdrop: #ece8e3;
    --card-black: #000000;
    --card-white: #ffffff;
    --charcoal: #2b2727;
    --faint-grey: #333333;
    --brand-grey: #707070;
    --crimson: #b8173a;
    --ink: #1e1e1e;
  }
  html, body {
    margin: 0;
    padding: 0;
    width: 1200px;
    height: 960px;
    overflow: hidden;
    background: var(--backdrop);
  }
  .canvas {
    position: relative;
    width: 1200px;
    height: 960px;
  }
  .card {
    position: absolute;
    overflow: hidden;
    box-shadow: 0 6px 16px rgba(0,0,0,0.25);
  }

  /* Front */
  .card-front {
    left: 64px; top: 50px; width: 708px; height: 426px;
    background: var(--card-black);
  }
  .front-decoration {
    position: absolute;
    left: 24px; top: 22px; width: 384px; height: 390px;
    border-radius: 44px;
    background: var(--faint-grey);
    opacity: 0.85;
  }
  .front-notch {
    position: absolute;
    top: 108px; width: 26px; height: 92px;
    background: var(--card-white);
  }
  .front-notch.left { left: 0; border-radius: 0 10px 10px 0; }
  .front-notch.right { right: 0; border-radius: 10px 0 0 10px; }
  .front-brand {
    position: absolute;
    left: 101px; top: 98px;
    display: flex; align-items: center; gap: 40px;
  }
  .brand-square {
    width: 113px; height: 113px;
    border-radius: 16px;
    background: var(--crimson);
  }
  .front-brand .brand-name {
    font-family: "Quicksand", sans-serif;
    font-weight: 500;
    font-size: 54px;
    color: var(--brand-grey);
    letter-spacing: 0.5px;
  }

  /* Back */
  .card-back {
    left: 418px; top: 494px; width: 710px; height: 426px;
    background: var(--card-white);
  }
  .back-tab {
    position: absolute;
    background: var(--charcoal);
    box-shadow: 0 3px 8px rgba(0,0,0,0.35);
  }
  .back-tab.top { left: 60px; top: -12px; width: 182px; height: 50px; border-radius: 14px; }
  .back-tab.bottom { left: 60px; top: 316px; width: 186px; height: 130px; border-radius: 16px; }
  .back-tab.side { left: -10px; top: 104px; width: 30px; height: 90px; border-radius: 8px; }
  .back-brand {
    position: absolute;
    left: 69px; top: 80px; width: 167px;
    display: flex; flex-direction: column; align-items: center; gap: 14px;
  }
  .back-brand .brand-square {
    width: 120px; height: 120px; border-radius: 18px;
  }
  .back-brand .brand-name {
    font-family: "PT Sans", sans-serif;
    font-size: 22px;
    color: var(--crimson);
    white-space: nowrap;
  }
  .name-bar {
    position: absolute;
    left: 306px; top: 103px; width: 404px; height: 93px;
    background: var(--charcoal);
    border-radius: 8px 0 0 8px;
    box-shadow: 0 8px 12px rgba(0,0,0,0.3);
    display: flex; align-items: center;
    padding-left: 56px; box-sizing: border-box;
  }
  .name-bar .person-name {
    font-family: "PT Sans", sans-serif;
    font-size: 44px;
    color: var(--card-white);
  }
  .rule {
    position: absolute;
    left: 296px; width: 414px; height: 3px;
    background: linear-gradient(90deg, rgba(0,0,0,0) 0%, rgba(0,0,0,0.22) 30%, rgba(0,0,0,0.22) 85%, rgba(0,0,0,0) 100%);
  }
  .rule.upper { top: 245px; }
  .rule.lower { top: 300px; }
  .contact {
    position: absolute;
    left: 360px;
    font-family: "PT Sans", sans-serif;
    color: var(--ink);
    margin: 0;
  }
  .website { top: 257px; font-size: 25px; letter-spacing: 0.5px; }
  .abn { top: 308px; font-size: 23px; }
  .phones {
    top: 345px; list-style: none; padding: 0;
    font-size: 15px; line-height: 24px;
  }
</style>
</head>
<body>
<main class="canvas">
  <section class="card card-front" aria-label="Card front">
    <div class="front-decoration" aria-hidden="true"></div>
    <div class="front-notch left"></div>
    <div class="front-notch right"></div>
    <div class="front-brand">
      <div class="brand-square" aria-hidden="true"></div>
      <span class="brand-name">Lumoren Match</span>
    </div>
  </section>

  <section class="card card-back" aria-label="Card back">
    <div class="back-tab top"></div>
    <div class="back-tab side"></div>
    <div class="back-tab bottom"></div>
    <div class="back-brand">
      <div class="brand-square" aria-hidden="true"></div>
      <span class="brand-name">Lumoren Match</span>
    </div>
    <div class="name-bar"><span class="person-name">Teo Marlowick</span></div>
    <div class="rule upper"></div>
    <p class="contact website">www.lumoren-match.example</p>
    <div class="rule lower"></div>
    <p class="contact abn">ABN 90817263</p>
    <ul class="contact phones">
      <li>+482710365 (Singapore)</li>
      <li>+615093284 (Australia)</li>
      <li>+790428153 (Amerika)</li>
    </ul>
  </section>
</main>
</body>
</html>
```